" Venda de joias online. Joias exclusivas. Encomenda de joias. Compra de joias, ou utilização das peças que não servem mais como crédito para peças novas. "

```html
<!DOCTYPE html>
<html lang="pt-BR">
<head>
<meta charset="utf-8">
<title>Assinatura de e-mail – Valmore Joias</title>
<link href="https://fonts.googleapis.com/css2?family=Montserrat:wght@400;500;700&display=swap" rel="stylesheet">
<style>
  :root {
    --page-bg: #ececec;
    --card-black: #0b0b0b;
    --gold: #c9a35a;
    --white: #ffffff;
    --soft-white: #e6e6e6;
  }
  html, body {
    margin: 0;
    padding: 0;
    width: 1200px;
    height: 1200px;
    overflow: hidden;
    background: var(--page-bg);
    font-family: "Montserrat", sans-serif;
  }
  .canvas {
    width: 1200px;
    height: 1200px;
    display: flex;
    align-items: center;
    justify-content: center;
  }
  .signature-card {
    position: relative;
    width: 1000px;
    height: 500px;
    background: var(--card-black);
    border-radius: 18px 60px 18px 60px;
    box-sizing: border-box;
  }
  .brand {
    position: absolute;
    left: 40px;
    width: 440px;
    top: 0;
    bottom: 0;
    display: flex;
    align-items: center;
    justify-content: center;
    gap: 16px;
  }
  .brand-mark {
    width: 26px;
    height: 26px;
    flex: none;
    background: var(--gold);
  }
  .brand-name {
    color: var(--white);
    font-weight: 500;
    font-size: 40px;
    letter-spacing: 0;
    line-height: 1;
    white-space: nowrap;
  }
  .divider {
    position: absolute;
    left: 520px;
    top: 70px;
    bottom: 70px;
    width: 3px;
    background: var(--gold);
  }
  .contact {
    position: absolute;
    right: 50px;
    top: 42px;
    width: 400px;
    text-align: right;
    color: var(--soft-white);
    font-size: 19px;
    line-height: 1.4;
  }
  .contact p { margin: 0; }
  .contact-name {
    color: var(--gold);
    font-weight: 700;
    font-size: 34px;
    line-height: 1.1;
  }
  .contact-role { font-size: 17px; margin-bottom: 26px !important; }
  .contact-group { margin-bottom: 22px; }
</style>
</head>
<body>
  <main class="canvas">
    <section class="signature-card">
      <div class="brand">
        <div class="brand-mark"></div>
        <div class="brand-name">Valmore Joias</div>
      </div>
      <div class="divider"></div>
      <div class="contact">
        <p class="contact-name">NOME COMPLETO</p>
        <p class="contact-role">cargo ocupacional</p>
        <div class="contact-group">
          <p>+00 (00) 0000 0000</p>
          <p>+00 (00) 0000 0000</p>
        </div>
        <div class="contact-group">
          <p>www.seusite.com.br</p>
          <p>facebook.com/valmorejoias</p>
          <p>email contato@ contato.com</p>
        </div>
        <div>
          <p>Endereço | Av. Nome | Nº</p>
          <p>Cidade | CEP | UF | Brasil</p>
        </div>
      </div>
    </section>
  </main>
</body>
</html>
```